Soccer Club Site Redesign

We are a suburban youth soccer club in need of a web site redesign. Our current site’s look/feel is outdated and is in need of a more modern look. What we are looking for is a design layout that will accommodate the current functionality we have for the site and give us an updated modern look. The deliverable for this project will be .psd file that can be converted to an html theme file for Wordpress. We will take care of the conversion and handle the html coding/javascript functionality.
Take a look at our current site to get an idea of what we offer and the current layout we have.
http://www.torvelkicks.org
Our club hosts youth recreational soccer, traveling soccer and two large soccer tournaments during the year. We also sponsor a number of training clinics. Our site serves a couple primary purposes:
1. Parents learn how/where/when to sign up their child for the leagues we offer.
2. Parents learn dates/times of various events the club offers.
3. Other soccer clubs get information on the tournaments we offer, sign up for the tournaments etc.
We do a pretty good job of presenting information about the various events/leagues available and how to sign up for them, but we want to do a better job of presenting a calendar where parents can quickly find dates/times of various events. Ideally, we would like to incorporate a news section (like we currently have), with a calendar and the use of more images on the home page. We understand screen space is limited but would incorporate jquery/javascript widgets to hide/show info and maybe an ‘imagebox’ for the additional images.
Here are a few sites with ideas that we liked:
http://sports.brenwickcollege.edu/ (Look at the Upcoming Events calendar on the page)
http://www.fennlowfutbol.com/ (look at the Upcoming Events calendar in the right column and the image box in the main content area)
http://www.rundlekick.com/index.php (Like the look and use of images)
http://www.qvfootyclub.com/ (imagebox use)
http://www.sarvapuckclub.org/ ( hockey website but like the use of crisp header graphics)
http://www.delvingpuckers.com/ (another hockey site, like the calendar used)
That should give you a pretty good idea of what we are looking for. The new design will need to accommodate the existing functionality of the site. Our logo (which is attached) should be incorporated into the site….otherwise we are open to your design ideas.

```html
<!DOCTYPE html>
<html lang="en">
<head>
<meta charset="utf-8">
<title>Torvel Soccer Club</title>
<link href="https://fonts.googleapis.com/css2?family=Montserrat:wght@400;500;600;700&family=Bree+Serif&family=Arimo:wght@400;700&display=swap" rel="stylesheet">
<style>
:root{
  --ink:#1b1b1b;
  --topbar:#151515;
  --blue:#1aa0dc;
  --blue-dark:#0e86c2;
  --navy:#1d3b6e;
  --orange:#f7941d;
  --sidebar:#1c1c1c;
  --panel:#10263d;
  --panel-line:#1f4a70;
  --grey-text:#333;
  --row-line:#e3e3e3;
  --muted:#9a9a9a;
  --white:#fff;
}
*{box-sizing:border-box;margin:0;padding:0}
html,body{width:959px;height:1200px;overflow:hidden}
body{
  position:relative;
  font-family:"Arimo",Arial,sans-serif;
  color:var(--ink);
  background:radial-gradient(ellipse at 50% 30%,#f4f4f4 0%,#d9d9d9 55%,#b9b9b9 100%);
}
.topbar{position:absolute;left:0;top:0;width:959px;height:38px;background:var(--topbar);border-bottom:1px solid #2a2a2a}
.weather{position:absolute;left:542px;top:9px;display:flex;align-items:center;gap:6px;font-family:"Montserrat",sans-serif;font-weight:700;font-size:9px;color:var(--white)}
.weather .temp{color:var(--orange);font-size:15px}
.account{position:absolute;left:733px;top:12px;display:flex;align-items:center;gap:5px;font-family:"Montserrat",sans-serif;font-size:10px;font-weight:600;color:var(--white)}
.account a{color:var(--blue);text-decoration:none}

.brand{position:absolute;left:130px;top:26px;width:80px;display:flex;flex-direction:column;align-items:center;gap:5px;text-align:center;font-family:"Montserrat",sans-serif;font-weight:700;font-size:12px;line-height:1.15;color:var(--navy)}
.brand .dot{width:34px;height:34px;border-radius:50%;background:var(--navy)}

.utility-nav{position:absolute;left:239px;top:96px;width:608px;display:flex;justify-content:space-between;font-family:"Montserrat",sans-serif;font-size:8.5px;font-weight:500;color:#222;letter-spacing:.2px}

.nav-accent{position:absolute;left:113px;top:120px;width:734px;height:7px;background:var(--topbar)}
.nav-accent::before{content:"";position:absolute;left:0;top:0;width:80px;height:7px;background:var(--orange)}
.main-nav{position:absolute;left:113px;top:127px;width:734px;height:37px;background:linear-gradient(#27aee6,var(--blue-dark));display:flex;align-items:center;font-family:"Montserrat",sans-serif;font-weight:600;font-size:13px;color:var(--white)}
.main-nav span{padding:0 0 0 22px}
.main-nav .current{background:linear-gradient(#40b9ec,#1596d3);height:37px;display:flex;align-items:center;padding:0 20px 0 20px;width:80px}
.main-nav span:nth-child(2){padding-left:20px}

.content{position:absolute;left:113px;top:164px;width:486px;height:954px;background:var(--white)}
.sidebar{position:absolute;left:599px;top:164px;width:248px;height:954px;background:var(--sidebar)}

.slider{position:absolute;left:7px;top:8px;width:472px;height:283px;background:#123}
.slide-photo{position:absolute;left:0;top:0;width:472px;height:223px;background:linear-gradient(120deg,#5f7f3e 0%,#8fa75a 35%,#c2cf8f 60%,#4f6b2c 100%)}
.slide-quote{position:absolute;left:30px;top:158px;width:420px;text-align:center;font-family:"Montserrat",sans-serif;font-weight:600;font-size:14px;line-height:1.1;color:var(--white);text-shadow:0 1px 3px rgba(0,0,0,.8)}
.thumbs{position:absolute;left:0;top:223px;width:472px;height:60px;background:#1b2a36;display:flex;align-items:center;gap:14px;padding-left:8px}
.thumbs .active-tab{position:absolute;left:0;top:0;width:60px;height:60px;background:var(--orange)}
.thumbs .active-tab::before{content:"";position:absolute;left:23px;top:-7px;border:7px solid transparent;border-top:0;border-bottom-color:var(--orange)}
.thumb{position:relative;width:44px;height:44px;border:2px solid #d8d8d8}
.t1{background:linear-gradient(#6f9a4a,#8c5b8a)}.t2{background:linear-gradient(#e8d04a,#4b7b2f)}
.t3{background:linear-gradient(#3d6fbf,#9cb6dc)}.t4{background:linear-gradient(#d33b3b,#4f7e33)}
.t5{background:linear-gradient(#4c8a3a,#c23434)}.t6{background:linear-gradient(#7a5da3,#5d8f3e)}
.t7{background:linear-gradient(#2c2c3c,#3f7b35)}.t8{background:linear-gradient(#b9c2c9,#e3a33b)}

.section-title{font-family:"Bree Serif",serif;font-size:16px;color:var(--navy);letter-spacing:.3px}
.events-head{position:absolute;left:7px;top:306px;width:472px;display:flex;justify-content:space-between;align-items:baseline}
.events-head .full{font-family:"Bree Serif",serif;font-size:11.5px;color:var(--orange)}
.events{position:absolute;left:7px;top:328px;width:472px;border-collapse:collapse;font-size:9.3px;color:var(--grey-text)}
.events .date-row td{background:var(--orange);color:var(--white);font-style:italic;height:17px;padding:0 8px;font-size:8.5px}
.events th{background:#ececec;height:17px;text-align:left;font-weight:700;font-size:9px;padding:0 8px}
.events td{height:34px;padding:0 8px;border-bottom:1px solid var(--row-line);line-height:1.25;vertical-align:middle}
.events .time{width:56px;padding-right:0}
.events .loc{width:96px}
.coverage{display:flex;gap:9px;align-items:center}

.gallery-title{position:absolute;left:9px;top:772px}
.gallery{position:absolute;left:10px;top:795px;width:466px;height:133px;border:1px solid #e4e4e4;border-bottom:3px solid #e9e9e9}
.gallery .arrow{position:absolute;top:54px;width:18px;height:18px;border-radius:50%;background:var(--white);box-shadow:0 0 3px rgba(0,0,0,.4);display:flex;align-items:center;justify-content:center}
.gallery .prev{left:-7px}.gallery .next{right:-7px}
.g-items{position:absolute;left:19px;top:16px;display:flex;gap:15px}
.g-item{width:96px;height:96px;background:var(--white);padding:4px;box-shadow:0 3px 6px rgba(0,0,0,.25)}
.g-item div{width:100%;height:100%}
.g1{background:linear-gradient(#4d8a3a,#d43a4a)}.g2{background:linear-gradient(#3f7c30,#cc3838)}
.g3{background:linear-gradient(#2f5ea8,#7aa94f)}.g4{background:linear-gradient(#d8c34b,#5a8a3c)}

.side-head{height:36px;display:flex;align-items:center;gap:7px;padding-left:12px;font-family:"Montserrat",sans-serif;font-weight:600;font-size:14.5px;color:var(--white);background:linear-gradient(90deg,#2b2b2b,#1c1c1c)}
.side-head b{color:var(--blue);font-weight:600}
.ball{width:12px;height:12px;border-radius:50%;background:var(--white);border:3px solid #777}
.news{list-style:none;padding:12px 14px 0 12px}
.news li{position:relative;padding-left:16px;font-size:10px;line-height:1.5;color:var(--white);margin-bottom:13px}
.news li::before{content:"→";position:absolute;left:0;top:0;color:var(--orange);font-weight:700}
.results-head{position:absolute;left:0;top:290px;width:248px}
.results{position:absolute;left:0;top:334px;width:248px;height:247px;background:var(--panel)}
.result{height:62px;padding:8px 16px;border-bottom:1px solid var(--panel-line);background:linear-gradient(90deg,#153455,#0d2136);font-size:10px;line-height:1.45;color:var(--white)}
.result strong{color:var(--orange);font-family:"Montserrat",sans-serif;font-weight:600;font-size:9.8px}
.scrollbar{position:absolute;right:0;top:0;width:9px;height:247px;background:#0b4a87}
.sponsors-head{position:absolute;left:0;top:601px;width:248px}
.sponsor-logos{position:absolute;left:0;top:660px;width:248px;display:flex;justify-content:center;gap:30px}
.sponsor{width:72px;height:50px;background:var(--white);display:flex;align-items:center;justify-content:center;font-family:"Montserrat",sans-serif;font-weight:700;font-size:13px;color:#1c1c1c}
.banner{position:absolute;left:0;width:248px;height:88px}
.banner-leagues{top:739px;background:linear-gradient(90deg,#1f3a18 0%,#3c6a25 50%,#6a5c20 100%)}
.banner-tournaments{top:846px;background:linear-gradient(90deg,#8a8f95 0%,#5d636a 55%,#2e3338 100%)}
.banner-text{position:absolute;left:12px;top:8px;font-family:"Montserrat",sans-serif;font-weight:700;font-size:13px;line-height:1.26;color:#b7d74a;text-transform:uppercase}
.banner-text .w{color:#efe6c4}
.banner-tournaments .banner-text{top:44px;color:var(--white);font-weight:500;font-size:13px;line-height:1.2}

.footer{position:absolute;left:113px;top:1141px;width:734px;height:41px;background:var(--topbar);display:flex;justify-content:space-between;align-items:center;padding:0 16px;font-size:9px;color:var(--white)}
</style>
</head>
<body>
<header class="topbar">
  <div class="weather">WEATHER FORECAST
    <svg width="34" height="30" viewBox="0 0 34 30" aria-hidden="true"><circle cx="19" cy="12" r="7" fill="#f7c221"/><g stroke="#f7c221" stroke-width="2"><line x1="19" y1="0" x2="19" y2="3"/><line x1="29" y1="12" x2="32" y2="12"/><line x1="27" y1="4" x2="29" y2="2"/><line x1="11" y1="4" x2="9" y2="2"/></g><ellipse cx="14" cy="22" rx="11" ry="6" fill="#d9dee4"/></svg>
    <span class="temp">34° F</span></div>
  <div class="account">
    <svg width="12" height="12" viewBox="0 0 12 12" aria-hidden="true"><circle cx="6" cy="3.5" r="3" fill="#ddd"/><path d="M0 12c0-4 3-5 6-5s6 1 6 5z" fill="#ddd"/></svg>
    <a>Sign In</a> or <a>Register</a></div>
</header>

<div class="brand"><span class="dot"></span>Torvel Soccer Club</div>

<nav class="utility-nav">
  <span>ABOUT US</span><span>FORMS</span><span>CALENDAR</span><span>TEAM MANAGER</span><span>VOLUNTEERS</span><span>CONTACT US</span><span>SPONSORS</span><span>LINKS</span>
</nav>

<div class="nav-accent"></div>
<nav class="main-nav">
  <span class="current">Home</span><span>Traveling</span><span style="padding-left:34px">Recreational</span><span style="padding-left:38px">Tournaments</span><span style="padding-left:38px">Referees</span><span style="padding-left:38px">Field Maps</span><span style="padding-left:38px">Coaches</span>
</nav>

<main class="content">
  <section class="slider">
    <div class="slide-photo" role="img" aria-label="Two youth players challenging for a ball in midair on a grass pitch"></div>
    <p class="slide-quote">"Neque porro quisquam est qui dolorem ipsum it amet, consectetur, adipisci velit..."</p>
    <div class="thumbs">
      <div class="active-tab"></div>
      <div class="thumb t1" role="img" aria-label="Match action thumbnail"></div>
      <div class="thumb t2" role="img" aria-label="Players celebrating thumbnail"></div>
      <div class="thumb t3" role="img" aria-label="Team in blue thumbnail"></div>
      <div class="thumb t4" role="img" aria-label="Players in red thumbnail"></div>
      <div class="thumb t5" role="img" aria-label="Match action thumbnail"></div>
      <div class="thumb t6" role="img" aria-label="Match action thumbnail"></div>
      <div class="thumb t7" role="img" aria-label="Player dribbling thumbnail"></div>
      <div class="thumb t8" role="img" aria-label="Goalkeeper dive thumbnail"></div>
    </div>
  </section>

  <div class="events-head"><h2 class="section-title">UPCOMING EVENTS</h2><span class="full">FULL SCHEDULE</span></div>
  <table class="events">
    <tr class="date-row"><td colspan="5">Friday, November 2</td></tr>
    <tr><th>Sport</th><th>Event</th><th colspan="2">Time - Location</th><th>Coverage</th></tr>
    <tr><td>Lorem ipsum dolor sit<br>amet, consec</td><td>Lpsum sit amet<br>consec</td><td class="time">6:00 p.m.</td><td class="loc">Ashmere, Wis.</td><td><div class="coverage"><svg width="11" height="9" viewBox="0 0 11 9"><path d="M0 3h2l3-3v9L2 6H0z" fill="#bbb"/><path d="M7 2q2 2.5 0 5M8.5 1q3 3.5 0 7" stroke="#bbb" fill="none"/></svg><svg width="11" height="8" viewBox="0 0 11 8"><rect y="1" width="7" height="6" fill="#bbb"/><path d="M7 4l4-3v6z" fill="#bbb"/></svg><svg width="9" height="9" viewBox="0 0 9 9"><rect x="0" y="5" width="2" height="4" fill="#bbb"/><rect x="3.5" y="2.5" width="2" height="6.5" fill="#bbb"/><rect x="7" y="0" width="2" height="9" fill="#bbb"/></svg></div></td></tr>
    <tr><td>Lorem ipsum dolor sit<br>amet, consec</td><td>Lpsum sit amet<br>consec</td><td class="time">6:00 p.m.</td><td class="loc">Ashmere, Wis.</td><td><div class="coverage"><svg width="11" height="9" viewBox="0 0 11 9"><path d="M0 3h2l3-3v9L2 6H0z" fill="#bbb"/><path d="M7 2q2 2.5 0 5M8.5 1q3 3.5 0 7" stroke="#bbb" fill="none"/></svg><svg width="11" height="8" viewBox="0 0 11 8"><rect y="1" width="7" height="6" fill="#bbb"/><path d="M7 4l4-3v6z" fill="#bbb"/></svg><svg width="9" height="9" viewBox="0 0 9 9"><rect x="0" y="5" width="2" height="4" fill="#bbb"/><rect x="3.5" y="2.5" width="2" height="6.5" fill="#bbb"/><rect x="7" y="0" width="2" height="9" fill="#bbb"/></svg></div></td></tr>
    <tr><td>Lorem ipsum dolor sit<br>amet, consec</td><td>Lpsum sit amet<br>consec</td><td class="time">6:00 p.m.</td><td class="loc">Ashmere, Wis.</td><td><div class="coverage"><svg width="11" height="9" viewBox="0 0 11 9"><path d="M0 3h2l3-3v9L2 6H0z" fill="#bbb"/><path d="M7 2q2 2.5 0 5M8.5 1q3 3.5 0 7" stroke="#bbb" fill="none"/></svg><svg width="11" height="8" viewBox="0 0 11 8"><rect y="1" width="7" height="6" fill="#bbb"/><path d="M7 4l4-3v6z" fill="#bbb"/></svg><svg width="9" height="9" viewBox="0 0 9 9"><rect x="0" y="5" width="2" height="4" fill="#bbb"/><rect x="3.5" y="2.5" width="2" height="6.5" fill="#bbb"/><rect x="7" y="0" width="2" height="9" fill="#bbb"/></svg></div></td></tr>
    <tr><td>Lorem ipsum dolor sit<br>amet, consec</td><td>Lpsum sit amet<br>consec</td><td class="time">6:00 p.m.</td><td class="loc">Ashmere, Wis.</td><td><div class="coverage"><svg width="11" height="9" viewBox="0 0 11 9"><path d="M0 3h2l3-3v9L2 6H0z" fill="#bbb"/><path d="M7 2q2 2.5 0 5M8.5 1q3 3.5 0 7" stroke="#bbb" fill="none"/></svg><svg width="11" height="8" viewBox="0 0 11 8"><rect y="1" width="7" height="6" fill="#bbb"/><path d="M7 4l4-3v6z" fill="#bbb"/></svg><svg width="9" height="9" viewBox="0 0 9 9"><rect x="0" y="5" width="2" height="4" fill="#bbb"/><rect x="3.5" y="2.5" width="2" height="6.5" fill="#bbb"/><rect x="7" y="0" width="2" height="9" fill="#bbb"/></svg></div></td></tr>
    <tr><td>Lorem ipsum dolor sit<br>amet, consec</td><td>Lpsum sit amet<br>consec</td><td class="time">6:00 p.m.</td><td class="loc">Ashmere, Wis.</td><td><div class="coverage"><svg width="11" height="9" viewBox="0 0 11 9"><path d="M0 3h2l3-3v9L2 6H0z" fill="#bbb"/><path d="M7 2q2 2.5 0 5M8.5 1q3 3.5 0 7" stroke="#bbb" fill="none"/></svg><svg width="11" height="8" viewBox="0 0 11 8"><rect y="1" width="7" height="6" fill="#bbb"/><path d="M7 4l4-3v6z" fill="#bbb"/></svg><svg width="9" height="9" viewBox="0 0 9 9"><rect x="0" y="5" width="2" height="4" fill="#bbb"/><rect x="3.5" y="2.5" width="2" height="6.5" fill="#bbb"/><rect x="7" y="0" width="2" height="9" fill="#bbb"/></svg></div></td></tr>
    <tr><td>Lorem ipsum dolor sit<br>amet, consec</td><td>Lpsum sit amet<br>consec</td><td class="time">6:00 p.m.</td><td class="loc">Ashmere, Wis.</td><td><div class="coverage"><svg width="11" height="9" viewBox="0 0 11 9"><path d="M0 3h2l3-3v9L2 6H0z" fill="#bbb"/><path d="M7 2q2 2.5 0 5M8.5 1q3 3.5 0 7" stroke="#bbb" fill="none"/></svg><svg width="11" height="8" viewBox="0 0 11 8"><rect y="1" width="7" height="6" fill="#bbb"/><path d="M7 4l4-3v6z" fill="#bbb"/></svg><svg width="9" height="9" viewBox="0 0 9 9"><rect x="0" y="5" width="2" height="4" fill="#bbb"/><rect x="3.5" y="2.5" width="2" height="6.5" fill="#bbb"/><rect x="7" y="0" width="2" height="9" fill="#bbb"/></svg></div></td></tr>
    <tr><td>Lorem ipsum dolor sit<br>amet, consec</td><td>Lpsum sit amet<br>consec</td><td class="time">6:00 p.m.</td><td class="loc">Ashmere, Wis.</td><td><div class="coverage"><svg width="11" height="9" viewBox="0 0 11 9"><path d="M0 3h2l3-3v9L2 6H0z" fill="#bbb"/><path d="M7 2q2 2.5 0 5M8.5 1q3 3.5 0 7" stroke="#bbb" fill="none"/></svg><svg width="11" height="8" viewBox="0 0 11 8"><rect y="1" width="7" height="6" fill="#bbb"/><path d="M7 4l4-3v6z" fill="#bbb"/></svg><svg width="9" height="9" viewBox="0 0 9 9"><rect x="0" y="5" width="2" height="4" fill="#bbb"/><rect x="3.5" y="2.5" width="2" height="6.5" fill="#bbb"/><rect x="7" y="0" width="2" height="9" fill="#bbb"/></svg></div></td></tr>
    <tr><td>Lorem ipsum dolor sit<br>amet, consec</td><td>Lpsum sit amet<br>consec</td><td class="time">6:00 p.m.</td><td class="loc">Ashmere, Wis.</td><td><div class="coverage"><svg width="11" height="9" viewBox="0 0 11 9"><path d="M0 3h2l3-3v9L2 6H0z" fill="#bbb"/><path d="M7 2q2 2.5 0 5M8.5 1q3 3.5 0 7" stroke="#bbb" fill="none"/></svg><svg width="11" height="8" viewBox="0 0 11 8"><rect y="1" width="7" height="6" fill="#bbb"/><path d="M7 4l4-3v6z" fill="#bbb"/></svg><svg width="9" height="9" viewBox="0 0 9 9"><rect x="0" y="5" width="2" height="4" fill="#bbb"/><rect x="3.5" y="2.5" width="2" height="6.5" fill="#bbb"/><rect x="7" y="0" width="2" height="9" fill="#bbb"/></svg></div></td></tr>
    <tr><td>Lorem ipsum dolor sit<br>amet, consec</td><td>Lpsum sit amet<br>consec</td><td class="time">6:00 p.m.</td><td class="loc">Ashmere, Wis.</td><td><div class="coverage"><svg width="11" height="9" viewBox="0 0 11 9"><path d="M0 3h2l3-3v9L2 6H0z" fill="#bbb"/><path d="M7 2q2 2.5 0 5M8.5 1q3 3.5 0 7" stroke="#bbb" fill="none"/></svg><svg width="11" height="8" viewBox="0 0 11 8"><rect y="1" width="7" height="6" fill="#bbb"/><path d="M7 4l4-3v6z" fill="#bbb"/></svg><svg width="9" height="9" viewBox="0 0 9 9"><rect x="0" y="5" width="2" height="4" fill="#bbb"/><rect x="3.5" y="2.5" width="2" height="6.5" fill="#bbb"/><rect x="7" y="0" width="2" height="9" fill="#bbb"/></svg></div></td></tr>
    <tr><td>Lorem ipsum dolor sit<br>amet, consec</td><td>Lpsum sit amet<br>consec</td><td class="time">6:00 p.m.</td><td class="loc">Ashmere, Wis.</td><td><div class="coverage"><svg width="11" height="9" viewBox="0 0 11 9"><path d="M0 3h2l3-3v9L2 6H0z" fill="#bbb"/><path d="M7 2q2 2.5 0 5M8.5 1q3 3.5 0 7" stroke="#bbb" fill="none"/></svg><svg width="11" height="8" viewBox="0 0 11 8"><rect y="1" width="7" height="6" fill="#bbb"/><path d="M7 4l4-3v6z" fill="#bbb"/></svg><svg width="9" height="9" viewBox="0 0 9 9"><rect x="0" y="5" width="2" height="4" fill="#bbb"/><rect x="3.5" y="2.5" width="2" height="6.5" fill="#bbb"/><rect x="7" y="0" width="2" height="9" fill="#bbb"/></svg></div></td></tr>
    <tr><td>Lorem ipsum dolor sit<br>amet, consec</td><td>Lpsum sit amet<br>consec</td><td class="time">6:00 p.m.</td><td class="loc">Ashmere, Wis.</td><td><div class="coverage"><svg width="11" height="9" viewBox="0 0 11 9"><path d="M0 3h2l3-3v9L2 6H0z" fill="#bbb"/><path d="M7 2q2 2.5 0 5M8.5 1q3 3.5 0 7" stroke="#bbb" fill="none"/></svg><svg width="11" height="8" viewBox="0 0 11 8"><rect y="1" width="7" height="6" fill="#bbb"/><path d="M7 4l4-3v6z" fill="#bbb"/></svg><svg width="9" height="9" viewBox="0 0 9 9"><rect x="0" y="5" width="2" height="4" fill="#bbb"/><rect x="3.5" y="2.5" width="2" height="6.5" fill="#bbb"/><rect x="7" y="0" width="2" height="9" fill="#bbb"/></svg></div></td></tr>
  </table>

  <h2 class="section-title gallery-title">PHOTO GALLERY</h2>
  <section class="gallery">
    <span class="arrow prev"><svg width="8" height="10" viewBox="0 0 8 10"><path d="M6 1L2 5l4 4" stroke="#222" stroke-width="2" fill="none"/></svg></span>
    <div class="g-items">
      <div class="g-item"><div class="g1" role="img" aria-label="Girls team in red jerseys"></div></div>
      <div class="g-item"><div class="g2" role="img" aria-label="Players contesting the ball on grass"></div></div>
      <div class="g-item"><div class="g3" role="img" aria-label="Boys in blue celebrating"></div></div>
      <div class="g-item"><div class="g4" role="img" aria-label="Family with a soccer ball"></div></div>
    </div>
    <span class="arrow next"><svg width="8" height="10" viewBox="0 0 8 10"><path d="M2 1l4 4-4 4" stroke="#222" stroke-width="2" fill="none"/></svg></span>
  </section>
</main>

<aside class="sidebar">
  <h2 class="side-head"><span class="ball"></span><span><b>LATEST</b> NEWS</span></h2>
  <ul class="news">
    <li>Torvel High School Boys and Girls teams both win State Quarters...</li>
    <li>LVYSA Fall State Champion and Fall League Champions...</li>
    <li>Summer Travel 2013 - Roster Spots open: U11 and U12 Girls C3, U13 Boys C3...</li>
    <li>Elsa Marwick Memorial Youth Soccer Scholarship...</li>
    <li>2013 Summer Travel Registration/Team Formations...</li>
  </ul>

  <h2 class="side-head results-head"><span class="ball"></span><span><b>RECENT</b> RESULTS</span></h2>
  <div class="results">
    <div class="result"><strong>10.27 | Women's Cross Country</strong><br>at RVAC Championships<br>8th place (12 teams)</div>
    <div class="result"><strong>10.27 | Women's Cross Country</strong><br>at RVAC Championships<br>8th place (12 teams)</div>
    <div class="result"><strong>10.27 | Women's Cross Country</strong><br>at RVAC Championships<br>8th place (12 teams)</div>
    <div class="result"><strong>10.27 | Women's Cross Country</strong><br>at RVAC Championships<br>8th place (12 teams)</div>
    <div class="scrollbar"></div>
  </div>

  <h2 class="side-head sponsors-head"><span class="ball"></span><span><b>OUR</b> SPONSORS</span></h2>
  <div class="sponsor-logos">
    <div class="sponsor">LVYSA</div>
    <div class="sponsor">Strivo</div>
  </div>

  <div class="banner banner-leagues" role="img" aria-label="Trophy and soccer ball on a stadium pitch">
    <p class="banner-text">Sign up<br><span class="w">your</span> child<br><span class="w">for the</span><br>leagues<br><span class="w">we offer.</span></p>
  </div>
  <div class="banner banner-tournaments" role="img" aria-label="Player with a ball in a floodlit stadium">
    <p class="banner-text">SIGN UP FOR<br>THE TOURNAMENTS</p>
  </div>
</aside>

<footer class="footer">
  <span>Copyright © Torvel Soccer Club 2012</span>
  <span>Support@corvalert.com &nbsp;|&nbsp; Privacy Statement</span>
</footer>
</body>
</html>
```